Demolition Company Billboard Design 13 feet wide 15 feet high

This is my first billboard on a busy road. I want it to be professional but with some eye catching flair that matches by business which is a demoltion business and also list my services. My company slogan is also

"call hollick, watch it fall"

Target Market(s)

Home Ownerd and General Construction Companies

Industry/Entity Type

construction

Colors
0054AA
0677BA
7BADD7
CADEEF
E8F1F8

Requirements
Must have
• My services listed in the pictures my website and my phone number

```html
<!DOCTYPE html>
<html lang="en">
<head>
<meta charset="utf-8">
<title>Hollick Demolition Billboard</title>
<link rel="stylesheet" href="https://fonts.googleapis.com/css2?family=Oswald:wght@400;500&display=swap">
<style>
  :root {
    --backdrop: #8c8c8c;
    --board-top: #1b4a78;
    --board-mid: #2b3a52;
    --board-bottom: #252525;
    --ink-light: #ffffff;
    --ink-navy: #1d4a7c;
  }
  html, body {
    margin: 0;
    padding: 0;
    width: 1199px;
    height: 1200px;
    overflow: hidden;
    background: var(--backdrop);
  }
  .billboard {
    display: block;
    width: 1199px;
    height: 1200px;
  }
  .headline, .slogan, .contact, .brand-name {
    font-family: "Oswald", "Arial Narrow", sans-serif;
  }
  .headline { fill: var(--ink-light); font-weight: 400; }
  .headline--large { font-size: 118px; }
  .headline--small { font-size: 82px; }
  .slogan { fill: var(--ink-navy); font-size: 44px; font-weight: 400; }
  .slogan-band { fill: var(--ink-light); }
  .accent-shard { fill: var(--ink-light); }
  .contact { fill: var(--ink-light); font-weight: 500; font-size: 38px; }
  .brand-name { fill: var(--ink-light); font-size: 46px; font-weight: 400; letter-spacing: 2px; }
</style>
</head>
<body>
<svg class="billboard" viewBox="0 0 960 961" xmlns="http://www.w3.org/2000/svg" aria-label="Hollick Demolition billboard">
  <defs>
    <linearGradient id="board-fill" x1="0" y1="0" x2="0" y2="1">
      <stop offset="0" stop-color="var(--board-top)"/>
      <stop offset="0.5" stop-color="var(--board-mid)"/>
      <stop offset="1" stop-color="var(--board-bottom)"/>
    </linearGradient>
  </defs>

  <rect class="board" x="157" y="108" width="646" height="745" fill="url(#board-fill)"/>

  <!-- services -->
  <text class="headline headline--large" x="213" y="256" textLength="365" lengthAdjust="spacingAndGlyphs">INTERIOR</text>
  <text class="headline headline--large" x="213" y="377" textLength="375" lengthAdjust="spacingAndGlyphs">EXTERIOR</text>
  <text class="headline headline--small" x="213" y="467" textLength="385" lengthAdjust="spacingAndGlyphs">COMMERCIAL</text>

  <!-- slogan band -->
  <rect class="slogan-band" x="157" y="508" width="463" height="75"/>
  <text class="slogan" x="212" y="565" textLength="392" lengthAdjust="spacingAndGlyphs">CALL HOLLICK, WATCH IT FALL</text>

  <!-- accent shards -->
  <polygon class="accent-shard" points="803,110 803,140 690,330 768,562 676,330"/>
  <polygon class="accent-shard" points="157,690 157,726 296,652 430,668 296,634"/>

  <!-- brand -->
  <text class="brand-name" x="640" y="698" text-anchor="middle">HOLLICK</text>

  <!-- contact -->
  <text class="contact" x="212" y="757" textLength="200" lengthAdjust="spacingAndGlyphs">412-555-0187</text>
  <text class="contact" x="212" y="801" textLength="342" lengthAdjust="spacingAndGlyphs">www.hollickdemo.com</text>
</svg>
</body>
</html>
```